Change color scheme of existing flyers

Hello! We recently re-branded our company with an awesome logo from Kelvo Market.
We changed our color scheme from Orange/Black to Red/Blue/Gray as you will see in the attachments.
We have a 4 page flyer that we need to incorporate the new colors into and have them look nice.
The pages are bound so the colors must flow well from page to page.
Please don't just replace logo, change orange to red, and submit. I designed the current flyers and can do that in 10 minutes. I'm looking for some great ideas to implement and make the flyers look as good as the new logo.:-)
This is a fun project but I have no time at the moment so I need your help.
I am attaching the old pdf versions and the new logo options for consideration.
Look forward to some creative input. Thanks!

Manufacturers

It Company

• Must have flow from page to page similar to old black/orange version
• We like the current configuration but are open to new designs also

```html
<!DOCTYPE html>
<html lang="en">
<head>
<meta charset="utf-8">
<title>Products and Services Flyer</title>
<link href="https://fonts.googleapis.com/css2?family=Arimo:ital,wght@0,400;0,700;1,400;1,700&display=swap" rel="stylesheet">
<style>
:root{
  --red:#e3141b;
  --ink:#111;
  --dark:#1d1d1d;
  --frame:#000;
  --band:#5e5e5e;
  --sky:#3db4ec;
  --paper:#fff;
}
*{box-sizing:border-box;margin:0;padding:0}
html,body{width:957px;height:1200px;overflow:hidden;background:var(--paper)}
body{font-family:"Arimo",Arial,sans-serif;color:var(--ink);position:relative}
.abs{position:absolute}
.backdrop{left:0;top:0;width:957px;height:1200px}
.catalog{left:36px;top:93px;width:827px;height:505px;background:var(--frame);border-radius:4px}
.product{top:108px;height:478px;background:var(--paper);padding:12px 10px 0 10px}
.product h2{font-size:21px;font-weight:400;color:var(--red);line-height:1}
.product h2 b{font-weight:700}
.visual{display:block;margin:0 auto;border-radius:2px}
.features{list-style:none;font-size:15.5px;line-height:19px;margin:0}
.specs{border-collapse:collapse;font-size:10.8px;line-height:11.6px;white-space:nowrap}
.specs th{font-weight:700;text-align:left;padding:0 6px 0 0}
.specs td{padding:0 6px 0 0}
.specs .n{text-align:right;padding:0 0 0 10px}
.capabilities{left:0;top:639px;width:957px;height:150px;background:var(--band)}
.capabilities h3{position:absolute;left:34px;top:10px;font-size:25px;font-weight:700;font-style:italic;color:var(--red);text-shadow:1px 1px 0 #fff}
.cap-col{position:absolute;top:38px;list-style:none;font-size:20.5px;line-height:23.5px;color:#000}
.card{top:816px;height:274px;background:var(--paper);border:4px solid #000;border-radius:34px;box-shadow:0 0 0 3px #777}
.card h4{font-size:24px;font-weight:400;color:var(--red);text-align:center;margin-bottom:6px}
.card p{font-size:14.2px;line-height:17.2px}
.footer{left:0;top:1123px;width:957px;height:54px;background:var(--sky);color:#fff;font-weight:700;font-size:23px;line-height:54px;padding-left:36px;letter-spacing:.1px}
</style>
</head>
<body>
<svg class="abs backdrop" viewBox="0 0 957 1200" aria-hidden="true">
  <defs>
    <linearGradient id="fade" x1="0" y1="0" x2="0" y2="1">
      <stop offset="0" stop-color="#bdbdbd"/><stop offset="1" stop-color="#2a2a2a"/>
    </linearGradient>
  </defs>
  <rect x="0" y="200" width="957" height="923" fill="var(--dark)"/>
  <path d="M0,200 C300,120 640,110 957,190 L957,240 L0,240Z" fill="var(--dark)"/>
  <path d="M0,195 C280,120 600,90 957,95 L957,190 C640,110 300,120 0,200Z" fill="url(#fade)"/>
  <path d="M0,30 C300,12 620,2 957,0 L957,10 C620,30 300,100 0,195Z" fill="var(--red)"/>
</svg>

<div class="abs catalog"></div>

<section class="abs product" style="left:50px;width:264px">
  <h2>Metal <b>Blind Boxes</b></h2>
  <div class="visual" role="img" aria-label="Galvanized blind box with dimensions A, B and C" style="width:150px;height:125px;margin-top:26px;background:linear-gradient(160deg,#e9eaec,#9fa3a8)"></div>
  <ul class="features" style="margin:38px 0 0 22px">
    <li>26ga Galvanized Sheet Metal</li><li>Mounting Flange</li><li>Fully Assembled</li><li>Custom Sizes Available</li>
  </ul>
  <table class="specs" style="margin:18px 0 0 0">
    <tr><th>Part#</th><th>Description</th><th class="n">A</th><th class="n">B</th><th class="n">C</th></tr>
    <tr><td>88-0804-11</td><td>Blind Box 08x04</td><td class="n">08</td><td class="n">04</td><td class="n">11</td></tr>
    <tr><td>88-1006-11</td><td>Blind Box 10x06</td><td class="n">10</td><td class="n">06</td><td class="n">11</td></tr>
    <tr><td>88-1010-11</td><td>Blind Box 10x10</td><td class="n">10</td><td class="n">10</td><td class="n">11</td></tr>
    <tr><td>88-1206-11</td><td>Blind Box 12x06</td><td class="n">12</td><td class="n">06</td><td class="n">11</td></tr>
    <tr><td>88-1212-11</td><td>Blind Box 12x12</td><td class="n">12</td><td class="n">12</td><td class="n">11</td></tr>
    <tr><td>88-1406-11</td><td>Blind Box 14x06</td><td class="n">14</td><td class="n">06</td><td class="n">11</td></tr>
    <tr><td>88-1414-11</td><td>Blind Box 14x14</td><td class="n">14</td><td class="n">14</td><td class="n">11</td></tr>
    <tr><td>88-1616-11</td><td>Blind Box 16x16</td><td class="n">16</td><td class="n">16</td><td class="n">11</td></tr>
    <tr><td>88-1818-11</td><td>Blind Box 18x18</td><td class="n">18</td><td class="n">18</td><td class="n">11</td></tr>
    <tr><td>88-2020-11</td><td>Blind Box 20x20</td><td class="n">20</td><td class="n">20</td><td class="n">11</td></tr>
    <tr><td>88-2424-11</td><td>Blind Box 24x24</td><td class="n">24</td><td class="n">24</td><td class="n">11</td></tr>
  </table>
</section>

<section class="abs product" style="left:319px;width:260px">
  <h2 style="font-weight:700;margin-left:8px">Condenser Bracket</h2>
  <div class="visual" role="img" aria-label="Black slotted condenser bracket with dimensions A and B" style="width:95px;height:160px;margin-top:12px;background:linear-gradient(180deg,#f4f4f4,#cfcfcf)"></div>
  <ul class="features" style="margin:14px 0 0 20px">
    <li>14ga Powder Coated Steel</li><li>Slotted Holes for Easy Install</li><li>Packaged 4 Brackets per Pack</li><li>&nbsp;(50 packs per box)</li><li>Engineering Documents</li><li>4" or 6" Heights Typical</li><li>Custom Sizes Available</li>
  </ul>
  <table class="specs" style="margin:18px 0 0 0">
    <tr><th>Part#</th><th style="padding-left:22px">Description</th><th class="n">A</th><th class="n">B</th></tr>
    <tr><td>32-CB1-04</td><td>Condenser Bracket 4"x1</td><td class="n">1"</td><td class="n">4"</td></tr>
    <tr><td>32-CB1-06</td><td>Condenser Bracket 6"x1</td><td class="n">1"</td><td class="n">6"</td></tr>
    <tr><td>32-CB2-06</td><td>Condenser Bracket 6"x2</td><td class="n">2"</td><td class="n">6"</td></tr>
  </table>
</section>

<section class="abs product" style="left:584px;width:264px">
  <h2 style="margin-left:8px"><b>Filter</b> Rack</h2>
  <div class="visual" role="img" aria-label="Galvanized filter rack frame with dimensions A and B" style="width:195px;height:90px;margin-top:44px;background:linear-gradient(180deg,#dfe2e6,#7d848c)"></div>
  <ul class="features" style="margin:38px 0 0 20px">
    <li>1" Filter Channel</li><li>Adjustable Design</li><li>Fits on Air Handler Bases</li><li>16ga Galvanized Tube</li><li>18ga Filter Channel</li><li>Custom Sizes Available</li>
  </ul>
  <table class="specs" style="margin:52px 0 0 0">
    <tr><th>Part#</th><th style="padding-left:18px">Description</th><th class="n">A</th><th class="n">B</th></tr>
    <tr><td>45-1425-22</td><td>Filter Rack Standard</td><td class="n">14-25</td><td class="n">22</td></tr>
    <tr><td>45-1930-22</td><td>Filter Rack Wide</td><td class="n">19-30</td><td class="n">22</td></tr>
  </table>
</section>

<section class="abs capabilities">
  <h3>What we can do...</h3>
  <ul class="cap-col" style="left:33px"><li>Truck Bins</li><li>Wall Brackets</li><li>Tank Stands</li><li>Fabrication</li></ul>
  <ul class="cap-col" style="left:314px"><li>Security Cages</li><li>Plenums</li><li>Welding</li><li>Powder Coating</li></ul>
  <ul class="cap-col" style="left:619px"><li>Ductboard Projects</li><li>Sheet Metal Projects</li><li>Condenser Wall Brackets</li><li>Air Distribution / Ventilation</li></ul>
</section>

<section class="abs card" style="left:42px;width:392px;padding:20px 34px 0 30px">
  <h4 style="margin-right:-10px">Terms and Conditions</h4>
  <p>1% 10 Days, NET 30<br>Custom items require 50% Deposit<br>NO Returns on Custom or Specialty Products<br>All Standard Returns Require Approval<br>Prices / Products subject to change w/o notice<br>No warranty of suitability for any particular purpose expressed or implied respecting these products. Customers modifying products or using for purposes other than the intended application shall, regardless of specific instruction, hold harmless Corvane, Inc for any and all claims, losses, or damages</p>
</section>

<section class="abs card" style="left:500px;width:366px;padding:20px 16px 0 42px">
  <h4 style="margin-left:-26px">Freight Policy</h4>
  <p>Paid on orders over $1500 shipped in Florida<br><i style="font-size:13px">&nbsp;*Florida Panhandle and X90 Program Excluded</i><br>Local North Florida Deliveries <b>No Charge</b><br>We also coordinate freight with customers utilizing <b><i>Branch</i></b> to <b><i>Branch</i></b> transit<br>Freight Policy subject to change w/o notice</p>
  <div role="img" aria-label="Wooden shipping pallet" style="width:150px;height:72px;margin:14px 0 0 52px;background:linear-gradient(160deg,#e9cfa3,#b88a55)"></div>
  <span class="abs" style="right:40px;bottom:12px;font-size:9px">09/15</span>
</section>

<svg class="abs" style="left:406px;top:900px" width="100" height="100" viewBox="0 0 100 100" aria-hidden="true">
  <polygon points="50,2 58,22 76,8 72,30 96,26 80,44 98,58 76,62 86,84 64,74 58,98 48,78 34,96 32,72 10,82 22,62 2,52 22,42 10,20 32,28 34,6 44,24" fill="var(--red)" stroke="#fff" stroke-width="2"/>
</svg>
<div class="abs" style="left:422px;top:930px;width:72px;text-align:center;color:#fff;font-weight:700;font-size:19px;line-height:20px;transform:rotate(-18deg)">Call<br>Today!</div>

<footer class="abs footer">1450-2 North Alder Street&nbsp; Springfield, FL&nbsp; 32208&nbsp; 555-210-0147&nbsp; Fax 555-210-0148</footer>
</body>
</html>
```